CREATE A BUSINESS CARD FOR A BOAT CLEANING SERVICE

WE ARE STARTING A NEW BOAT CLEANING BUSINESS. WE DIVE UNDERWATER TO CLEAN BOAT HULLS, JETTIES, UNDERWATER STRUCTURES ETC. WE ARE LOOKING FOR AN UPPERMARKET MODERN LOGO AND BUSINESS CARD AS ALOT OF OUR TARGET MARKET WILL BE HIGH END. YOU HAVE TO DESIGN A BUSINESS CARD AND LOGO SEPERATELY .
THE BUSINESS CARD DIMESNION MUST BE STANDARD SIZE.
The standard dimensions of a printed business card are 3.5 x 2 inches

Target Market(s)

UNDERWATER SERVICED

Industry/Entity Type

Business

Contact Information for Business Card

HALDEN UNDERWATER SERVICES

Font styles to use
Serif

Colors

Designer to choose colors to be used in the design.

Requirements
Must have
• HALDEN
Nice to have
• dark
Should not have
• more than 3 colors

```html
<!DOCTYPE html>
<html lang="en">
<head>
<meta charset="utf-8">
<title>Halden Underwater Service – Business Cards</title>
<link href="https://fonts.googleapis.com/css2?family=Jost:wght@400;500&display=swap" rel="stylesheet">
<style>
  :root {
    --sky: #5c93c4;
    --sea: #5aa2d9;
    --deep: #0a0a1c;
    --navy: #15162e;
    --steel: #6d7f99;
    --white: #ffffff;
    --ink: #1b1c3a;
  }
  * { margin: 0; padding: 0; box-sizing: border-box; }
  html, body { width: 1200px; height: 1200px; overflow: hidden; background: var(--white); }
  body { position: relative; font-family: "Jost", sans-serif; }

  .card {
    position: absolute;
    width: 520px;
    height: 297px;
    overflow: hidden;
    box-shadow: -6px -4px 10px rgba(0,0,0,0.45);
  }

  /* Front */
  .card-front {
    left: 110px; top: 260px;
    background: linear-gradient(to bottom, var(--sky) 0%, #2c3f5e 30%, var(--navy) 55%, var(--deep) 100%);
  }
  .front-rule {
    position: absolute; left: 0; right: 0; top: 186px;
    height: 1px; background: var(--steel); opacity: 0.7;
  }
  .front-name {
    position: absolute; left: 0; right: 0; top: 166px;
    text-align: center;
    font-size: 31px; font-weight: 400; letter-spacing: 0.62em;
    padding-left: 0.62em;
    color: var(--steel);
  }
  .front-name span { background: transparent; padding: 0 14px; }
  .front-tagline {
    position: absolute; left: 0; right: 0; top: 222px;
    text-align: center; color: var(--white);
    font-size: 13px; letter-spacing: 0.32em;
  }

  /* Back */
  .card-back {
    left: 580px; top: 510px;
    background: var(--white);
  }
  .back-sea { position: absolute; left: 0; top: 89px; width: 520px; height: 208px; }
  .back-brand {
    position: absolute; right: 26px; top: 46px;
    display: flex; align-items: center; gap: 18px;
  }
  .back-brand .mark {
    width: 22px; height: 22px; border-radius: 50%; background: var(--ink);
  }
  .back-brand .name {
    font-size: 31px; letter-spacing: 0.55em; margin-right: -0.55em; color: var(--ink);
  }
  .back-tagline {
    position: absolute; right: 26px; top: 102px;
    color: var(--white); font-size: 13px; letter-spacing: 0.3em;
  }
  .back-person, .back-phone, .back-email {
    position: absolute; left: 0; right: 0; text-align: center; color: var(--white);
  }
  .back-person { top: 162px; font-size: 16px; letter-spacing: 0.35em; }
  .back-phone { top: 219px; font-size: 16px; letter-spacing: 0.38em; }
  .back-email { top: 244px; font-size: 14px; letter-spacing: 0.3em; }
</style>
</head>
<body>
  <section class="card card-front" aria-label="Business card front">
    <div class="front-rule"></div>
    <div class="front-name"><span>HALDEN</span></div>
    <div class="front-tagline">UNDERWATER SERVICE</div>
  </section>

  <section class="card card-back" aria-label="Business card back">
    <svg class="back-sea" viewBox="0 0 520 208" preserveAspectRatio="none" aria-hidden="true">
      <defs>
        <linearGradient id="seaFill" x1="0" y1="0" x2="0" y2="1">
          <stop offset="0" stop-color="#5aa2d9"/>
          <stop offset="0.35" stop-color="#3b5d85"/>
          <stop offset="0.7" stop-color="#16193a"/>
          <stop offset="1" stop-color="#0a0a1c"/>
        </linearGradient>
        <linearGradient id="beam" x1="0" y1="0" x2="1" y2="0">
          <stop offset="0" stop-color="#8fb4d6" stop-opacity="0.5"/>
          <stop offset="1" stop-color="#8fb4d6" stop-opacity="0.15"/>
        </linearGradient>
      </defs>
      <rect width="520" height="208" fill="url(#seaFill)"/>
      <polygon points="0,30 520,72 520,92 0,30" fill="#7ea6cc" opacity="0.55"/>
      <polygon points="0,30 520,92 520,110 300,115" fill="url(#beam)"/>
    </svg>
    <div class="back-brand">
      <div class="mark"></div>
      <div class="name">HALDEN</div>
    </div>
    <div class="back-tagline">UNDERWATER SERVICE</div>
    <div class="back-person">Your Name</div>
    <div class="back-phone">123-555-1234</div>
    <div class="back-email">underwaterservice@haldendive.com</div>
  </section>
</body>
</html>
```